Business Card Design Project

We need a simple business card design that uses our current logo.
We need to have the current logo put into a high res format.
We need to have 1 card made with contact information.
We will supply the information for the 4 employees.
Industry/Entity Type
Business
Requirements
Must have
- The contact information is as follows:
Mark Dellweather
Producer/CEO
c. 949-555-0147
f. 650-555-0193
markd@lanternbay.example
Al Vostrand, CFO
c. 949-555-0162
f. 650-555-0193
alv@lanternbay.example
Peter Malvane, PR
c. 267-555-0128
f. 650-555-0193
pmalvane@lanternbay.example
Tim Garrowby, Producer
c. 949-555-0184
f. 650-555-0193
timg@lanternbay.example
The address for all cards is:
318 W Calle Norvento #2715, San Clemente, CA 92681

```html
<!DOCTYPE html>
<html lang="en">
<head>
<meta charset="utf-8">
<title>Lantern Bay Media — Business Cards</title>
<link rel="stylesheet" href="https://fonts.googleapis.com/css2?family=Source+Sans+3:wght@400;600;700&display=swap">
<style>
  :root {
    --bg: #ece6de;
    --red: #e20f0f;
    --blue: #00bdf2;
    --yellow: #e2e000;
    --orange: #ff7200;
    --white: #ffffff;
    --ink: #2a2a1a;
    --band: rgba(255, 255, 255, 0.18);
    --card-w: 240px;
    --card-h: 375px;
  }
  * { box-sizing: border-box; margin: 0; padding: 0; }
  html, body { width: 1200px; height: 900px; overflow: hidden; }
  body {
    background: var(--bg);
    font-family: "Source Sans 3", "Helvetica Neue", Arial, sans-serif;
    position: relative;
  }
  .card {
    position: absolute;
    width: var(--card-w);
    height: var(--card-h);
    box-shadow: 0 4px 14px rgba(0, 0, 0, 0.28);
    overflow: hidden;
  }
  .card--red { background: var(--red); }
  .card--blue { background: var(--blue); }
  .card--yellow { background: var(--yellow); }
  .card--orange { background: var(--orange); }

  /* Front side */
  .front__rule {
    position: absolute;
    height: 1.5px;
    background: var(--white);
  }
  .front__rule--top-left { left: 8px; width: 62px; top: 150px; }
  .front__rule--top-right { right: 8px; width: 62px; top: 155px; }
  .front__rule--bottom { left: 8px; right: 8px; top: 198px; }
  .front__logo {
    position: absolute;
    left: 0; right: 0; top: 162px;
    display: flex; align-items: center; justify-content: center; gap: 7px;
    color: var(--white);
    font-weight: 700;
    font-size: 23px;
    letter-spacing: 0.5px;
    text-transform: uppercase;
  }
  .front__logo-mark { width: 11px; height: 11px; background: var(--white); }
  .front__tagline {
    position: absolute;
    left: 0; right: 0; top: 202px;
    text-align: center;
    color: var(--white);
    font-size: 7.5px;
    font-weight: 600;
  }
  .front__services {
    position: absolute;
    left: 0; right: 0; top: 213px;
    text-align: center;
    color: rgba(255, 255, 255, 0.6);
    font-size: 5.5px;
  }

  /* Back side */
  .back { color: var(--white); text-align: center; }
  .back--dark { color: var(--ink); }
  .back__name { position: absolute; left: 0; right: 0; top: 80px; font-size: 15px; font-weight: 600; }
  .back__title { position: absolute; left: 0; right: 0; top: 100px; font-size: 9px; opacity: 0.8; }
  .back__band {
    position: absolute; left: 0; right: 0; top: 150px; height: 100px;
    background: var(--band);
  }
  .back__contact { position: absolute; left: 0; right: 0; top: 168px; font-size: 8.5px; line-height: 1.3; }
  .back__contact-head { font-size: 13px; font-weight: 600; margin-bottom: 2px; }
  .back__web { position: absolute; left: 0; right: 0; top: 295px; font-size: 13px; }
  .back__footer { position: absolute; left: 8px; bottom: 8px; font-size: 5px; }
</style>
</head>
<body>

  <!-- Card fronts -->
  <section class="card card--red" style="left:90px; top:120px;">
    <span class="front__rule front__rule--top-left"></span>
    <span class="front__rule front__rule--top-right"></span>
    <div class="front__logo"><span class="front__logo-mark"></span>Lantern Bay Media</div>
    <span class="front__rule front__rule--bottom"></span>
    <p class="front__tagline">visual communication agency</p>
    <p class="front__services">graphic design | branding | advertising | web design</p>
  </section>

  <section class="card card--blue" style="left:165px; top:195px;">
    <span class="front__rule front__rule--top-left"></span>
    <span class="front__rule front__rule--top-right"></span>
    <div class="front__logo"><span class="front__logo-mark"></span>Lantern Bay Media</div>
    <span class="front__rule front__rule--bottom"></span>
    <p class="front__tagline">visual communication agency</p>
    <p class="front__services">graphic design | branding | advertising | web design</p>
  </section>

  <section class="card card--yellow" style="left:235px; top:300px;">
    <span class="front__rule front__rule--top-left"></span>
    <span class="front__rule front__rule--top-right"></span>
    <div class="front__logo"><span class="front__logo-mark"></span>Lantern Bay Media</div>
    <span class="front__rule front__rule--bottom"></span>
    <p class="front__tagline">visual communication agency</p>
    <p class="front__services">graphic design | branding | advertising | web design</p>
  </section>

  <section class="card card--orange" style="left:310px; top:365px;">
    <span class="front__rule front__rule--top-left"></span>
    <span class="front__rule front__rule--top-right"></span>
    <div class="front__logo"><span class="front__logo-mark"></span>Lantern Bay Media</div>
    <span class="front__rule front__rule--bottom"></span>
    <p class="front__tagline">visual communication agency</p>
    <p class="front__services">graphic design | branding | advertising | web design</p>
  </section>

  <!-- Card backs -->
  <section class="card card--orange back" style="left:890px; top:75px;">
    <h2 class="back__name">Mark Dellweather</h2>
    <p class="back__title">Producer/CEO</p>
    <div class="back__band"></div>
    <div class="back__contact">
      <p class="back__contact-head">Contact</p>
      <p>C: 949-555-0147</p>
      <p>F: 650-555-0193</p>
      <p>318 W Calle Norvento #2715, San Clemente, CA 92681</p>
      <p>E: markd@lanternbay.example</p>
    </div>
    <p class="back__web">www.lanternbay.example</p>
    <p class="back__footer">brand development | design | visual communication</p>
  </section>

  <section class="card card--red back" style="left:820px; top:160px;">
    <h2 class="back__name">Peter Malvane</h2>
    <p class="back__title">PR</p>
    <div class="back__band"></div>
    <div class="back__contact">
      <p class="back__contact-head">Contact</p>
      <p>C: 267-555-0128</p>
      <p>F: 650-555-0193</p>
      <p>318 W Calle Norvento #2715, San Clemente, CA 92681</p>
      <p>E: pmalvane@lanternbay.example</p>
    </div>
    <p class="back__web">www.lanternbay.example</p>
    <p class="back__footer">brand development | design | visual communication</p>
  </section>

  <section class="card card--blue back back--dark" style="left:730px; top:245px;">
    <h2 class="back__name">Tim Garrowby</h2>
    <p class="back__title">Producer</p>
    <div class="back__band"></div>
    <div class="back__contact">
      <p class="back__contact-head">Contact</p>
      <p>C: 949-555-0184</p>
      <p>F: 650-555-0193</p>
      <p>318 W Calle Norvento #2715, San Clemente, CA 92681</p>
      <p>E: timg@lanternbay.example</p>
    </div>
    <p class="back__web">www.lanternbay.example</p>
    <p class="back__footer">brand development | design | visual communication</p>
  </section>

  <section class="card card--yellow back back--dark" style="left:635px; top:325px;">
    <h2 class="back__name">Al Vostrand</h2>
    <p class="back__title">CFO</p>
    <div class="back__band"></div>
    <div class="back__contact">
      <p class="back__contact-head">Contact</p>
      <p>C: 949-555-0162</p>
      <p>F: 650-555-0193</p>
      <p>318 W Calle Norvento #2715, San Clemente, CA 92681</p>
      <p>E: alv@lanternbay.example</p>
    </div>
    <p class="back__web">www.lanternbay.example</p>
    <p class="back__footer">brand development | design | visual communication</p>
  </section>

</body>
</html>
```